Quillmen Letterhead

I would like to create a letterhead file similar to what we have but in MS Word format. Right now this is a PDF and is not functional

```html
<!DOCTYPE html>
<html lang="en">
<head>
<meta charset="utf-8">
<title>Quillmen Hockey Club Letterhead</title>
<link rel="stylesheet" href="https://fonts.googleapis.com/css2?family=Arimo:wght@400;700&display=swap">
<style>
  :root {
    --navy: #141a44;
    --gold: #f6b818;
    --ink: #5a5a5a;
    --paper: #ffffff;
    --white: #ffffff;
  }
  * { margin: 0; padding: 0; box-sizing: border-box; }
  html, body { width: 849px; height: 1200px; overflow: hidden; background: var(--paper); }
  body { font-family: "Arimo", Arial, sans-serif; }
  .letterhead { position: relative; width: 849px; height: 1200px; background: var(--paper); }

  .header-band {
    position: absolute; left: 0; top: 40px; width: 849px; height: 105px;
    background: var(--navy);
  }
  .accent-left {
    position: absolute; left: 76px; top: 40px; width: 29px; height: 164px;
    background: var(--gold);
  }
  .club-mark {
    position: absolute; left: 118px; top: 62px;
    display: flex; align-items: center; gap: 8px;
  }
  .club-mark-dot {
    width: 34px; height: 34px; border-radius: 50%; background: var(--gold);
  }
  .club-mark-name {
    font-size: 14px; font-weight: 400; color: var(--white); letter-spacing: 0.5px;
  }
  .club-name {
    position: absolute; left: 262px; top: 58px;
    font-size: 19px; font-weight: 700; color: var(--white); letter-spacing: 0.3px;
  }
  .club-town {
    position: absolute; left: 262px; top: 84px;
    font-size: 16px; color: var(--gold); letter-spacing: 0.5px;
  }
  .contact { position: absolute; right: 82px; top: 46px; list-style: none; }
  .contact li {
    display: flex; align-items: center; justify-content: flex-end;
    height: 34px; font-size: 11px; color: var(--white);
  }
  .contact svg { width: 22px; height: 22px; margin-left: 22px; fill: var(--gold); }

  .letter-body {
    position: absolute; left: 156px; top: 338px; width: 537px;
    font-size: 10.5px; line-height: 16.5px; color: var(--ink);
  }
  .letter-body p { margin-bottom: 17px; }
  .letter-body .greeting { margin-bottom: 4px; }
  .letter-body .closing { margin-top: 2px; margin-bottom: 14px; }

  .footer-band {
    position: absolute; left: 0; top: 1033px; width: 849px; height: 29px;
    background: var(--navy);
  }
  .accent-right {
    position: absolute; left: 680px; top: 1005px; width: 28px; height: 79px;
    background: var(--gold);
  }
</style>
</head>
<body>
<div class="letterhead">
  <header>
    <div class="header-band"></div>
    <div class="accent-left"></div>
    <div class="club-mark">
      <span class="club-mark-dot"></span>
      <span class="club-mark-name">QUILLMEN</span>
    </div>
    <div class="club-name">QUILLMEN HOCKEY CLUB</div>
    <div class="club-town">LAKEPORT</div>
    <ul class="contact">
      <li>555-010-0247
        <svg viewBox="0 0 24 24" aria-hidden="true"><path d="M12 1a11 11 0 1 0 0 22 11 11 0 0 0 0-22zm0 2a9 9 0 1 1 0 18 9 9 0 0 1 0-18zM8.6 6.5l1.6-.3 1.2 2.8-1.2 1a8 8 0 0 0 3.8 3.8l1-1.2 2.8 1.2-.3 1.6c-.2.8-1 1.3-1.8 1.1A10 10 0 0 1 7.5 8.3c-.2-.8.3-1.6 1.1-1.8z"/></svg>
      </li>
      <li>12 Harbor Road, Lakeport AB
        <svg viewBox="0 0 24 24" aria-hidden="true"><path d="M12 2 1 11h3v10h6v-6h4v6h6V11h3z"/></svg>
      </li>
      <li>lakeportquillmen.ca
        <svg viewBox="0 0 24 24" aria-hidden="true"><path d="M2 5h20v14H2zm2 2v.5l8 5.5 8-5.5V7zm0 3v7h16v-7l-8 5.5z"/></svg>
      </li>
    </ul>
  </header>

  <main class="letter-body">
    <p class="greeting">Hello Sir,</p>
    <p>Lorem ipsum dolor sit amet, consectetur adipiscing elit, sed do eiusmod tempor incididunt ut labore et dolore magna aliqua. Ut enim ad minim veniam, quis nostrud exercitation ullamco laboris nisi ut aliquip ex ea commodo consequat. Duis aute irure dolor in reprehenderit in voluptate velit esse cillum dolore eu fugiat nulla pariatur. Excepteur sint occaecat cupidatat non proident, sunt in culpa qui officia deserunt mollit anim id est laborum.</p>
    <p>Lorem ipsum dolor sit amet, consectetur adipiscing elit, sed do eiusmod tempor incididunt ut labore et dolore magna aliqua. Ut enim ad minim veniam, quis nostrud exercitation ullamco laboris nisi ut aliquip ex ea commodo consequat. Duis aute irure dolor in reprehenderit in voluptate velit esse cillum dolore eu fugiat nulla pariatur. Excepteur sint occaecat cupidatat non proident, sunt in culpa qui officia deserunt mollit anim id est laborum. Lorem ipsum dolor sit amet, consectetur adipiscing elit, sed do eiusmod tempor incididunt ut labore et dolore magna aliqua. Ut enim ad minim veniam, quis nostrud exercitation ullamco laboris.</p>
    <p>“Lorem ipsum dolor sit amet, consectetur adipiscing elit, sed do eiusmod tempor incididunt ut labore et dolore magna aliqua. Ut enim ad minim veniam, quis nostrud exercitation ullamco laboris nisi ut aliquip ex ea commodo consequat. Duis aute irure dolor in reprehenderit in voluptate velit esse cillum dolore eu fugiat nulla pariatur. Excepteur sint occaecat cupidatat non proident, sunt in culpa qui officia deserunt mollit anim id est laborum.”</p>
    <p>Lorem ipsum dolor sit amet, consectetur adipiscing elit, sed do eiusmod tempor incididunt ut labore et dolore magna aliqua. Ut enim ad minim veniam, quis nostrud exercitation ullamco laboris nisi ut aliquip ex ea commodo consequat. Duis aute irure dolor in reprehenderit in voluptate velit esse cillum dolore eu fugiat nulla pariatur. Excepteur sint occaecat cupidatat non proident, sunt in culpa qui officia deserunt mollit anim id est laborum.</p>
    <p class="closing">Thank You</p>
    <p>Dana Kell</p>
  </main>

  <footer>
    <div class="footer-band"></div>
    <div class="accent-right"></div>
  </footer>
</div>
</body>
</html>
```